washable paper bags and accessories

We are three sisters who have discovered a mutual love of bags made from washable paper. It is a brand new business venture for bags, handbags, cosmetic bags, and home storage solutions and décor all made with washable paper.
We would like to have white crumpled paper as a background for both sides. Front of card with the words "plume douce cloth" only in "bohemian typewriter regular" font. Back of card with appointment style format for our next pop up stall
Target Market(s)
mums, females
Industry/Entity Type
Business
Contact Information for Business Card
ph: 0487215364
email:plumedoucecloth@mailbarrow.com

```html
<!DOCTYPE html>
<html lang="en">
<head>
<meta charset="utf-8">
<title>plume douce cloth – appointment card</title>
<link href="https://fonts.googleapis.com/css2?family=Source+Sans+3:wght@400;600&display=swap" rel="stylesheet">
<style>
  :root {
    --paper-light: #ececec;
    --paper-mid: #c4c4c4;
    --paper-dark: #939393;
    --band-blue: #0000f0;
    --band-edge: #ff1a1a;
    --ink-black: #0a0a0a;
    --ink-blue: #0a0af0;
    --ink-red: #f01e1e;
    --ink-white: #ffffff;
    --body-face: "Source Sans 3", "Helvetica Neue", Arial, sans-serif;
  }
  html, body {
    margin: 0;
    padding: 0;
    width: 1200px;
    height: 700px;
    overflow: hidden;
    background: #ffffff;
  }
  .card {
    position: relative;
    width: 1200px;
    height: 700px;
    overflow: hidden;
    font-family: var(--body-face);
  }
  .paper-texture {
    position: absolute;
    inset: 0;
    background:
      linear-gradient(125deg, rgba(255,255,255,0.25) 0%, rgba(0,0,0,0) 40%, rgba(0,0,0,0.08) 70%, rgba(255,255,255,0.15) 100%),
      radial-gradient(ellipse at 55% 45%, var(--paper-light) 0%, var(--paper-mid) 60%, var(--paper-dark) 100%);
  }
  .brand-band {
    position: absolute;
    left: 0;
    top: 97px;
    width: 1200px;
    height: 82px;
    box-sizing: border-box;
    background: var(--band-blue);
    border-top: 3px solid var(--band-edge);
    border-bottom: 3px solid var(--band-edge);
    display: flex;
    align-items: center;
    justify-content: center;
  }
  .brand-name {
    margin: 0;
    font-family: var(--body-face);
    font-weight: 600;
    font-size: 60px;
    line-height: 1;
    color: var(--ink-white);
    white-space: nowrap;
  }
  .field-line {
    position: absolute;
    margin: 0;
    white-space: nowrap;
    line-height: 1;
  }
  .blank {
    display: inline-block;
    border-bottom: 2px solid var(--ink-black);
    vertical-align: baseline;
    height: 1px;
  }
  .client-line {
    left: 117px;
    top: 250px;
    font-size: 44px;
    color: var(--ink-black);
  }
  .blank-name { width: 590px; margin: 0 10px 0 2px; }
  .day-row {
    position: absolute;
    left: 0;
    top: 320px;
    width: 1200px;
    height: 36px;
    list-style: none;
    margin: 0;
    padding: 0;
  }
  .day {
    position: absolute;
    top: 0;
    display: flex;
    align-items: center;
    font-size: 32px;
    line-height: 36px;
    color: var(--ink-blue);
  }
  .day svg { margin-right: 10px; }
  .schedule-line {
    left: 117px;
    top: 385px;
    font-size: 44px;
    color: var(--ink-red);
  }
  .blank-date { width: 309px; margin-right: 33px; }
  .blank-time { width: 330px; }
  .meridiem {
    position: absolute;
    left: 989px;
    top: 378px;
    margin: 0;
    padding: 0;
    list-style: none;
    font-size: 29px;
    line-height: 22px;
    font-weight: 600;
    color: var(--ink-blue);
  }
  .meridiem li { white-space: nowrap; }
  .meridiem .blank { width: 34px; margin-left: 4px; }
  .contact {
    position: absolute;
    display: flex;
    align-items: center;
    margin: 0;
    color: var(--ink-blue);
    white-space: nowrap;
  }
  .contact-phone { left: 380px; top: 528px; font-size: 50px; }
  .contact-email { left: 216px; top: 594px; font-size: 47px; }
  .contact svg { margin-right: 6px; }
</style>
</head>
<body>
<main class="card">
  <div class="paper-texture" role="img" aria-label="White crumpled paper texture filling the background"></div>

  <header class="brand-band">
    <h1 class="brand-name">plume douce cloth</h1>
  </header>

  <p class="field-line client-line">Mr./Ms.<span class="blank blank-name"></span>has appt. on</p>

  <ul class="day-row">
    <li class="day" style="left:116px"><svg width="30" height="30" viewBox="0 0 30 30"><circle cx="15" cy="15" r="12.5" fill="#fff" stroke="#0a0a0a" stroke-width="2.5"/></svg>MON.</li>
    <li class="day" style="left:279px"><svg width="30" height="30" viewBox="0 0 30 30"><circle cx="15" cy="15" r="12.5" fill="#fff" stroke="#0a0a0a" stroke-width="2.5"/></svg>TUE.</li>
    <li class="day" style="left:422px"><svg width="30" height="30" viewBox="0 0 30 30"><circle cx="15" cy="15" r="12.5" fill="#fff" stroke="#0a0a0a" stroke-width="2.5"/></svg>WED.</li>
    <li class="day" style="left:576px"><svg width="30" height="30" viewBox="0 0 30 30"><circle cx="15" cy="15" r="12.5" fill="#fff" stroke="#0a0a0a" stroke-width="2.5"/></svg>THU.</li>
    <li class="day" style="left:725px"><svg width="30" height="30" viewBox="0 0 30 30"><circle cx="15" cy="15" r="12.5" fill="#fff" stroke="#0a0a0a" stroke-width="2.5"/></svg>FRI.</li>
    <li class="day" style="left:846px"><svg width="30" height="30" viewBox="0 0 30 30"><circle cx="15" cy="15" r="12.5" fill="#fff" stroke="#0a0a0a" stroke-width="2.5"/></svg>SAT.</li>
    <li class="day" style="left:980px"><svg width="30" height="30" viewBox="0 0 30 30"><circle cx="15" cy="15" r="12.5" fill="#fff" stroke="#0a0a0a" stroke-width="2.5"/></svg>SUN.</li>
  </ul>

  <p class="field-line schedule-line">Date:<span class="blank blank-date"></span>Time:<span class="blank blank-time"></span></p>

  <ul class="meridiem">
    <li>am<span class="blank"></span></li>
    <li>pm<span class="blank"></span></li>
  </ul>

  <p class="contact contact-phone">
    <svg width="58" height="60" viewBox="0 0 58 60" aria-label="Phone">
      <ellipse cx="29" cy="55" rx="20" ry="4" fill="#2a2af0"/>
      <path d="M10 50 L16 30 H42 L48 50 Z" fill="#4a6ad8" stroke="#0a0a40" stroke-width="2"/>
      <circle cx="29" cy="40" r="6" fill="#fff" stroke="#0a0a40" stroke-width="2"/>
      <path d="M6 26 Q8 10 29 8 Q50 10 52 26 L44 28 Q42 18 29 17 Q16 18 14 28 Z" fill="#4a6ad8" stroke="#0a0a40" stroke-width="2"/>
    </svg>: 0487215364
  </p>

  <p class="contact contact-email">
    <svg width="60" height="62" viewBox="0 0 60 62" aria-label="Email">
      <ellipse cx="24" cy="58" rx="14" ry="3.5" fill="#c01010"/>
      <rect x="16" y="24" width="16" height="32" rx="3" fill="#e01818"/>
      <rect x="30" y="10" width="28" height="20" fill="#e01818" stroke="#600" stroke-width="1.5"/>
      <path d="M30 10 L44 22 L58 10" fill="none" stroke="#600" stroke-width="1.5"/>
    </svg>:plumedoucecloth@mailbarrow.com
  </p>
</main>
</body>
</html>
```